New website for a commercial real estate consulting company

What we’re looking for in a new web site:
• Desktop and mobile friendly
• Clear navigation
• Strong graphics
• Professional appearance
• The ability to update it ourselves
• Site is for information purposes only – no transactions required
• Traffic counts – number of visits per page?
• A firm quote on costs to develop and launch
• SSL
Attached is a copy of the revised text we propose to use, including our new logo. (The pagination can be different than as shown.)
Our current website address is www.tamblinvaleadvisory.ca

```html
<!DOCTYPE html>
<html lang="en">
<head>
<meta charset="utf-8">
<title>Tamblin Vale Advisory</title>
<link rel="stylesheet" href="https://fonts.googleapis.com/css2?family=Oswald:wght@400;500;600&family=Open+Sans:wght@300;400;600&display=swap">
<style>
:root{
  --blue:#2b3894;
  --blue-dark:#1f2a7a;
  --ink:#111111;
  --text:#555a66;
  --grey-bg:#e6e6e8;
  --footer-bg:#ececee;
  --dark-band:#3b3f47;
  --white:#ffffff;
}
*{margin:0;padding:0;box-sizing:border-box}
html,body{width:1200px;height:3261px;overflow:hidden}
body{position:relative;background:var(--white);font-family:"Open Sans",Arial,sans-serif;color:var(--text)}
section,header,footer{position:absolute;left:0;width:1200px}
.abs{position:absolute}
h2{font-family:"Oswald",Arial,sans-serif;font-weight:500;color:var(--ink);font-size:44px;letter-spacing:.5px}

/* hero */
.hero{top:0;height:583px;background:linear-gradient(180deg,#5d6b7c 0%,#8d99a6 45%,#6f7a82 80%,#56605f 100%)}
.hero-photo{position:absolute;inset:0;background:linear-gradient(100deg,rgba(40,50,65,.55) 0%,rgba(120,140,160,.25) 45%,rgba(40,50,65,.5) 100%)}
.nav{position:absolute;top:12px;left:0;width:1200px;display:flex;justify-content:center;gap:38px}
.nav a{color:var(--white);text-decoration:none;font-size:15px;letter-spacing:2px;padding-bottom:10px;font-weight:400}
.nav a.active{border-bottom:2px solid var(--white)}
.hero-brand{position:absolute;top:110px;left:0;width:1200px;text-align:center;color:var(--white)}
.brand-mark{display:inline-block;width:50px;height:50px;border:2px solid var(--white);margin-bottom:10px}
.brand-name{font-family:"Oswald",Arial,sans-serif;font-size:28px;letter-spacing:3px;font-weight:400}
.hero-title{position:absolute;top:296px;width:1200px;text-align:center;font-family:"Oswald",Arial,sans-serif;font-weight:600;font-size:58px;color:var(--white);letter-spacing:2px}
.hero-points{position:absolute;top:404px;width:1200px;display:flex;justify-content:center;gap:70px}
.point{display:flex;align-items:center;gap:14px;color:var(--white);font-size:17px;letter-spacing:3px}
.chevron{position:absolute;top:528px;left:585px}

/* about */
.about{top:583px;height:532px}
.about h2{position:absolute;left:87px;top:80px}
.about-copy{position:absolute;left:87px;top:146px;width:555px;font-size:14.5px;line-height:1.6}
.about-copy p{margin-bottom:22px}
.about-copy strong{color:var(--blue);font-weight:600}
.years{position:absolute;left:704px;top:91px;width:407px;height:350px;background:linear-gradient(135deg,#c9cfe4 0%,#8e98c6 45%,#3e4a99 100%)}
.years-mark{position:absolute;right:16px;top:14px;width:24px;height:24px;border:2px solid var(--white)}
.years-num{position:absolute;left:30px;top:180px;font-family:"Oswald",Arial,sans-serif;font-size:68px;font-weight:600;color:var(--white);line-height:1}
.years-label{position:absolute;left:30px;top:258px;font-family:"Oswald",Arial,sans-serif;font-style:italic;font-size:28px;color:var(--white);line-height:1.2}

/* clients */
.clients{top:1115px;height:507px;background:var(--grey-bg)}
.clients-photo{position:absolute;left:0;top:0;width:717px;height:507px;background:linear-gradient(120deg,#f4f4f4 0%,#d9c3ad 45%,#b9987c 60%,#ececec 100%)}
.clients h2{position:absolute;left:720px;top:80px}
.client-list{position:absolute;left:722px;top:150px;list-style:none;font-size:14.5px;color:#333}
.client-list li{height:26.5px;padding-left:18px;position:relative}
.client-list li::before{content:"";position:absolute;left:0;top:6px;border-left:7px solid #333;border-top:5px solid transparent;border-bottom:5px solid transparent}
.clients-quote{position:absolute;left:722px;top:400px;font-family:"Oswald",Arial,sans-serif;font-style:italic;font-weight:500;font-size:19px;color:var(--blue)}

/* who we are */
.who{top:1622px;height:428px;background:var(--blue)}
.who-photo{position:absolute;right:0;top:0;width:700px;height:428px;background:linear-gradient(160deg,rgba(255,255,255,.12) 0%,rgba(255,255,255,.02) 60%,rgba(0,0,0,0) 100%)}
.who h2{position:absolute;left:87px;top:82px;color:var(--white)}
.who p{position:absolute;left:87px;top:148px;width:550px;color:var(--white);font-size:14.5px;line-height:1.6}
.btn{position:absolute;display:flex;align-items:center;justify-content:center;font-family:"Oswald",Arial,sans-serif;font-size:15px;letter-spacing:.5px;text-decoration:none}
.btn-light{left:87px;top:291px;width:174px;height:44px;background:var(--white);color:var(--blue)}

/* what we do */
.what{top:2050px;height:620px}
.what-band{position:absolute;left:0;top:330px;width:1200px;height:290px;background:linear-gradient(180deg,#3f434b,#2d3038)}
.what h2{position:absolute;width:1200px;text-align:center;top:80px}
.what-intro{position:absolute;left:210px;top:145px;width:780px;text-align:center;font-size:14.5px;line-height:1.6}
.services{position:absolute;left:124px;top:224px;display:flex}
.service{width:238px}
.service-img{height:170px}
.service-label{height:65px;display:flex;align-items:center;justify-content:center;font-family:"Oswald",Arial,sans-serif;font-size:18px;color:var(--white)}
.label-dark{background:#050505}
.label-blue{background:var(--blue)}
.what-outro{position:absolute;left:200px;top:506px;width:800px;text-align:center;font-size:14.5px;line-height:1.6;color:#d9dbe0}

/* events */
.events{top:2670px;height:330px}
.events-title{position:absolute;top:52px;width:1200px;text-align:center;font-family:"Oswald",Arial,sans-serif;font-weight:500;font-size:22px;color:var(--blue)}
.event-col{position:absolute;top:118px;border-left:3px solid var(--blue);padding-left:16px;height:42px}
.event-col h3{font-family:"Oswald",Arial,sans-serif;font-weight:500;font-size:16px;color:var(--ink);margin-bottom:4px}
.event-col li{list-style:none;font-size:13px;color:#333;line-height:1.55}
.btn-blue{left:513px;top:221px;width:174px;height:44px;background:var(--blue);color:var(--white)}

/* footer */
.footer{top:3000px;height:261px;background:var(--footer-bg)}
.footer-brand{position:absolute;left:87px;top:60px;display:flex;align-items:center;gap:10px}
.footer-brand .mark{width:22px;height:22px;background:var(--blue)}
.footer-brand span{font-family:"Oswald",Arial,sans-serif;font-size:18px;color:var(--blue);letter-spacing:1px}
.copyright{position:absolute;left:87px;top:180px;font-size:12px}
.footer h4{position:absolute;top:60px;font-family:"Oswald",Arial,sans-serif;font-weight:500;font-size:14px;color:var(--blue);letter-spacing:.5px}
.quick{position:absolute;left:385px;top:92px;list-style:none;font-size:12.5px;line-height:24px}
.contact{position:absolute;font-size:12.5px;line-height:18px}
.contact svg{position:absolute;left:-28px;top:2px}
</style>
</head>
<body>

<header class="hero">
  <div class="hero-photo" role="img" aria-label="Photo of a modern glass office tower seen from street level"></div>
  <nav class="nav">
    <a class="active" href="#">HOME</a>
    <a href="#">WHO WE ARE</a>
    <a href="#">WHAT WE DO</a>
    <a href="#">CONTACT US</a>
    <a href="#">INDUSTRY EVENTS CALENDAR</a>
  </nav>
  <div class="hero-brand">
    <span class="brand-mark"></span>
    <div class="brand-name">TAMBLIN VALE ADVISORY</div>
  </div>
  <h1 class="hero-title">LOREM IPSUM DUMMY</h1>
  <div class="hero-points">
    <div class="point">
      <svg width="40" height="40" viewBox="0 0 40 40" fill="none" stroke="#fff" stroke-width="2"><circle cx="20" cy="20" r="16"/><path d="M20 10l3 7h7l-5.5 4.5 2 7L20 24l-6.5 4.5 2-7L10 17h7z"/></svg>
      EXPERT
    </div>
    <div class="point">
      <svg width="40" height="40" viewBox="0 0 40 40" fill="none" stroke="#fff" stroke-width="2"><circle cx="14" cy="8" r="4"/><path d="M9 16h10v12h-2v10h-6V28H9z"/><path d="M28 14l1.5 3 3 .5-2.2 2 .6 3-2.9-1.5-2.9 1.5.6-3-2.2-2 3-.5z"/></svg>
      EXPERIENCED
    </div>
    <div class="point">
      <svg width="40" height="40" viewBox="0 0 40 40" fill="none" stroke="#fff" stroke-width="2"><circle cx="24" cy="14" r="9"/><path d="M24 9v10M21 11h5M21 17h5"/><path d="M4 30h8l6 3h10l6-5"/></svg>
      COST EFFECTIVE
    </div>
  </div>
  <svg class="chevron" width="30" height="18" viewBox="0 0 30 18" fill="none" stroke="#fff" stroke-width="2"><path d="M2 2l13 13L28 2"/></svg>
</header>

<section class="about">
  <h2>ABOUT US</h2>
  <div class="about-copy">
    <p><strong>Tamblin Vale Advisory</strong> is an independent consulting firm offering practical, hands-on assistance to the commercial real estate and commercial mortgage lending industries. We specialize in financial analysis, underwriting and financial due diligence.</p>
    <p>Working with us, you get top notch help when you need it – and only when you need it – one project at a time. Tamblin Vale Advisory has been providing expert, experienced and cost-effective service to the commercial real estate and commercial mortgage industries since 2001. We have worked on projects across Canada and the United States, and in every major property type.</p>
    <p>The foundation of our success has been our commitment to exceeding our clients' expectations, both in quality and in timeliness. We strive to go above and beyond on every assignment.</p>
  </div>
  <div class="years" role="img" aria-label="Photo of a glass curtain wall facade in blue tones">
    <span class="years-mark"></span>
    <div class="years-num">19</div>
    <div class="years-label">YEARS OF<br>EXPERIENCE</div>
  </div>
</section>

<section class="clients">
  <div class="clients-photo" role="img" aria-label="Photo of a team stacking hands together"></div>
  <h2>OUR CLIENTS INCLUDE</h2>
  <ul class="client-list">
    <li>Chartered banks</li>
    <li>Mortgage bankers</li>
    <li>Public REITs &amp; REOCs</li>
    <li>Private equity firms</li>
    <li>Family-owned real estate investment companies</li>
    <li>Life insurance companies</li>
    <li>Pension funds</li>
    <li>Non-bank lenders</li>
    <li>Brokerage firms</li>
  </ul>
  <div class="clients-quote">"REPUTATION IS THE CURRENCY OF THE 21ST CENTURY"</div>
</section>

<section class="who">
  <div class="who-photo" role="img" aria-label="Faint photo of a high-rise tower tinted blue"></div>
  <h2>WHO WE ARE</h2>
  <p>Maren has more than 30 years' senior experience in a wide range of property types. Her expertise encompasses all aspects of the financing, valuation, purchase and sale of commercial real estate. Prior to founding Tamblin Vale Advisory in 2001, Maren spent 16 years of her career in a variety of institutional roles, culminating in ten years as Vice-President, Property Investments of a Canadian life insurance company.</p>
  <a class="btn btn-light" href="#">READ MORE</a>
</section>

<section class="what">
  <div class="what-band" role="img" aria-label="Dark photo of city office buildings"></div>
  <h2>WHAT WE DO</h2>
  <p class="what-intro">Lorem Ipsum is simply dummy text of the printing and typesetting industry. Lorem Ipsum has been the industry's standard dummy text ever since the 1500s, when an unknown printer took a galley of type and scrambled.</p>
  <div class="services">
    <div class="service">
      <div class="service-img" role="img" aria-label="Photo of construction cranes against a blue sky" style="background:linear-gradient(180deg,#8fb2d6,#c9a06a)"></div>
      <div class="service-label label-dark">FOR OWNERS</div>
    </div>
    <div class="service">
      <div class="service-img" role="img" aria-label="Photo of eyeglasses resting on a building plan" style="background:linear-gradient(160deg,#3a6a8e,#b98a4e)"></div>
      <div class="service-label label-blue">FOR BUYERS</div>
    </div>
    <div class="service">
      <div class="service-img" role="img" aria-label="Photo of a desk with laptop, calculator and documents" style="background:linear-gradient(160deg,#6b4a32,#d8d4cc)"></div>
      <div class="service-label label-dark">FOR LENDERS</div>
    </div>
    <div class="service">
      <div class="service-img" role="img" aria-label="Photo of a business handshake" style="background:linear-gradient(160deg,#e9e9ea,#9aa0a8)"></div>
      <div class="service-label label-blue">FOR BROKERS</div>
    </div>
  </div>
  <p class="what-outro">Many desktop publishing packages and web page editors now use Lorem Ipsum as their default model text, and a search for 'lorem ipsum' will uncover many web sites still in their infancy.</p>
</section>

<section class="events">
  <div class="events-title">INDUSTRY EVENTS CALENDAR</div>
  <div class="event-col" style="left:87px">
    <h3>JANUARY 2019</h3>
    <ul><li>&gt;&nbsp; 27–29 Coastal Retail Forum</li></ul>
  </div>
  <div class="event-col" style="left:350px">
    <h3>FEBRUARY 2019</h3>
    <ul><li>&gt;&nbsp; 26 Capital Markets Summit</li></ul>
  </div>
  <div class="event-col" style="left:615px">
    <h3>MARCH 2019</h3>
    <ul><li>&gt;&nbsp; 6 Toronto Realty Women AGM</li><li>&gt;&nbsp; 27 Property Managers Spring Meet</li></ul>
  </div>
  <div class="event-col" style="left:880px">
    <h3>APRIL 2019</h3>
    <ul><li>&gt;&nbsp; 3 Toronto Building Owners AGM</li><li>&gt;&nbsp; 9 Realty Excellence Gala</li></ul>
  </div>
  <a class="btn btn-blue" href="#">VIEW ALL</a>
</section>

<footer class="footer">
  <div class="footer-brand"><span class="mark"></span><span>TAMBLIN VALE ADVISORY</span></div>
  <div class="copyright">© Copyright 2019. All Rights Reserved.</div>

  <h4 style="left:385px">QUICK LINKS</h4>
  <ul class="quick">
    <li>Home</li><li>Who We Are</li><li>What We Do</li><li>Contact Us</li><li>Industry Events Calendar</li>
  </ul>

  <h4 style="left:613px">CONTACT INFO</h4>
  <div class="contact" style="left:643px;top:92px">
    <svg width="14" height="18" viewBox="0 0 14 18"><path d="M7 0a7 7 0 0 0-7 7c0 5 7 11 7 11s7-6 7-11a7 7 0 0 0-7-7z" fill="#555a66"/><circle cx="7" cy="7" r="2.5" fill="#ececee"/></svg>
    Tamblin Vale Advisory<br>48 Kestrel Lane<br>Acton, Ontario &nbsp;L7J 0A4
  </div>
  <div class="contact" style="left:643px;top:150px">
    <svg width="16" height="16" viewBox="0 0 16 16"><rect x="1" y="3" width="14" height="11" rx="2" fill="#555a66"/><rect x="4" y="6" width="8" height="2" fill="#ececee"/><rect x="4" y="10" width="8" height="2" fill="#ececee"/></svg>
    905-555-0128
  </div>
  <div class="contact" style="left:826px;top:92px">
    Maren Holloway<br>Phone: 905-555-0171<br>Email: maren.holloway@tamblinvaleadvisory.ca
  </div>
  <div class="contact" style="left:826px;top:156px">
    Declan Ashby<br>Phone: 905-555-0192<br>Email: declan.ashby@tamblinvaleadvisory.ca
  </div>
</footer>

</body>
</html>
```